My name is Delia Forsythe,I want to create a web page for my personal dog grooming business. The name on the web page can be "Delia's Dog Grooming" I am located in San Antonio Texas. The page would help grow my customer base. Before and after pictures would display the quality of work that I do. On my page I can provide information about myself, my services, and pricing.
Updates

I have updated project to guaranteed pay

Please try to incorporate a schnauzer in an icon or logo. My dog is a schnauzer. THANKS!!!!!!!!!!!!

Target Market(s)

Dog Owners

Industry/Entity Type

Business

Requirements
Must have
• -A spot for before and after pictures.
-An about me section
-A section to make an appointment
Nice to have
• My favorite Color is purple. I think different shades of purple would be nice or purple with a light green

please incorporate a schnauzer in any icon or logo. My dog is a schnauzer.

```html
<!DOCTYPE html>
<html lang="en">
<head>
<meta charset="utf-8">
<title>Delia's Dog Grooming</title>
<link href="https://fonts.googleapis.com/css2?family=Arimo:ital,wght@0,400;1,400&family=PT+Sans:ital,wght@0,400;0,700;1,700&family=PT+Sans+Narrow:wght@700&family=Roboto+Condensed:wght@300;400&display=swap" rel="stylesheet">
<style>
:root{
  --purple-deep:#3d0a5c;
  --purple:#5e1587;
  --purple-bright:#7a22aa;
  --purple-text:#541873;
  --frame:#b76ed3;
  --green:#8fd61a;
  --green-dark:#5fae08;
  --ink:#222;
  --page:#f3f3f4;
  --white:#fff;
}
*{margin:0;padding:0;box-sizing:border-box}
html,body{width:942px;height:1200px;overflow:hidden}
body{position:relative;background:var(--page);font-family:"Arimo",Arial,sans-serif;color:var(--ink)}
.abs{position:absolute}
.header-band{left:0;top:0;width:942px;height:350px;
  background:radial-gradient(ellipse at 45% 30%,var(--purple-bright) 0%,var(--purple) 45%,var(--purple-deep) 100%)}
.brand-mark{left:38px;top:17px;width:110px;height:110px;border-radius:50%;background:var(--white);border:4px solid #d9c7e3}
.brand-name{left:160px;top:40px;font-family:"PT Sans",sans-serif;font-weight:700;color:var(--green);line-height:1}
.brand-name .main{display:block;font-size:42px}
.brand-name .sub{display:block;font-size:17px;margin:5px 0 0 20px;letter-spacing:.5px}
.call-photo{left:630px;top:8px;width:82px;height:76px;border-radius:6px;background:linear-gradient(#f2f2f2,#cfcfd3)}
.call-us{left:725px;top:16px;color:var(--white);font-family:"PT Sans",sans-serif;font-weight:700;line-height:1}
.call-us .label{font-size:18px}
.call-us .number{font-size:31px;margin-top:3px;letter-spacing:.5px}
.main-nav{left:384px;top:85px;width:521px;height:38px;border-radius:10px;
  background:linear-gradient(#fff,#e4e4e6);border:1px solid #bbb;display:flex;align-items:center;justify-content:space-around;
  font-family:"PT Sans",sans-serif;font-size:16px;color:#222}
.main-nav span+span{border-left:1px solid #aaa;padding-left:10px}
.slider{left:37px;top:143px;width:868px;height:282px;border-radius:10px;overflow:hidden;
  background:linear-gradient(#fafafa 0%,#ececee 55%,#d6d6d8 100%);border:3px solid #e6e6e8;box-shadow:0 14px 14px -8px rgba(0,0,0,.35)}
.slide-photo{border-radius:14px}
.slide-dog-a{left:58px;top:12px;width:230px;height:257px;background:linear-gradient(160deg,#8a929c,#5a616b)}
.slide-dog-b{left:460px;top:28px;width:348px;height:228px;background:linear-gradient(160deg,#6d6a6c,#8e7468)}
.arrow{position:absolute}
.share-bar{left:37px;top:462px;width:868px;height:66px;border-radius:10px;background:#f1f1f2;border:1px solid #dcdcdc}
.share-label{left:16px;top:21px;font-family:"PT Sans",sans-serif;font-size:18px;color:#333}
.share-dot{top:17px;width:30px;height:30px;border-radius:50%;background:linear-gradient(#b9b9c0,#8c8c96)}
.cta{left:615px;top:12px;width:221px;height:43px;border-radius:10px;background:linear-gradient(#b9f03a,var(--green-dark));
  box-shadow:0 3px 4px rgba(0,0,0,.3);font-family:"PT Sans Narrow",sans-serif;font-weight:700;font-size:21px;color:#1c2a04;text-align:center;line-height:43px;letter-spacing:.5px}
.panel{border:2px solid var(--frame);border-radius:8px;background:#f7f7f8;box-shadow:0 0 0 4px #fff,0 0 0 5px #e2e2e2}
.panel-title{font-family:"Roboto Condensed",sans-serif;font-weight:400;color:var(--purple-text);line-height:1.05}
.panel-title .small{font-size:22px;font-weight:300}
.panel-title .big{font-size:32px;font-weight:400}
.copy{font-size:12.8px;line-height:18.6px}
.copy .line{display:block;text-align:justify;text-align-last:justify;white-space:nowrap}
.copy .line.end{text-align-last:left}
.more{font-style:italic;color:var(--purple-text);text-decoration:underline;margin-left:4px}
.thumb{width:146px;height:101px;border-radius:6px;background:linear-gradient(#9aa0a6,#4c5057);box-shadow:0 2px 4px rgba(0,0,0,.35);overflow:hidden}
.thumb .tag{position:absolute;left:0;bottom:0;width:100%;height:20px;background:rgba(20,20,20,.75);color:#fff;font-size:12px;font-weight:700;text-align:center;line-height:20px}
.offer{left:37px;top:1000px;width:572px;height:71px;border-radius:8px;background:linear-gradient(#c5f54e,#7ccd10);border:1px solid #6aa60d}
.offer-photo{left:60px;top:992px;width:88px;height:88px;border-radius:50%;border:4px solid #fff;background:radial-gradient(#9a9ca0,#55585e);box-shadow:0 2px 5px rgba(0,0,0,.4)}
.offer-text{left:130px;top:4px;width:360px;font-family:"PT Sans",sans-serif;font-weight:700;font-size:18px;line-height:21px;color:var(--purple-text);text-align:center}
.offer-link{left:497px;top:48px;font-family:"PT Sans",sans-serif;font-weight:700;font-size:14px;color:#1c2a04;text-decoration:underline}
.footer{left:0;top:1097px;width:942px;height:103px;background:radial-gradient(ellipse at 50% 0%,var(--purple-bright),var(--purple-deep) 80%);color:#fff;font-size:11px}
.footer .legal{left:38px;top:40px;line-height:14px}
.footer .links{left:549px;top:48px;font-size:11.5px}
</style>
</head>
<body>

<div class="abs header-band"></div>

<div class="abs brand-mark"></div>
<div class="abs brand-name"><span class="main">DELIA'S</span><span class="sub">DOG GROOMING</span></div>

<div class="abs call-photo" role="img" aria-label="Photo of a dog wearing a call-centre headset"></div>
<div class="abs call-us"><div class="label">Call Us:</div><div class="number">021 5550148</div></div>

<nav class="abs main-nav"><span>Home</span><span>About Me</span><span>Services</span><span>Grooming</span><span>Gallery</span><span>Contact Me</span></nav>

<div class="abs slider">
  <div class="abs slide-photo slide-dog-a" role="img" aria-label="Groomed schnauzer standing in profile"></div>
  <div class="abs slide-photo slide-dog-b" role="img" aria-label="Two schnauzers lying down together"></div>
  <svg class="arrow" style="left:12px;top:124px" width="26" height="48" viewBox="0 0 26 48"><path d="M22 4 L5 24 L22 44" fill="none" stroke="#8a8a8f" stroke-width="4" stroke-linecap="round"/></svg>
  <svg class="arrow" style="left:826px;top:124px" width="26" height="48" viewBox="0 0 26 48"><path d="M4 4 L21 24 L4 44" fill="none" stroke="#8a8a8f" stroke-width="4" stroke-linecap="round"/></svg>
</div>

<div class="abs share-bar">
  <div class="abs share-label">Share with us on:</div>
  <div class="abs share-dot" style="left:175px"></div>
  <div class="abs share-dot" style="left:212px"></div>
  <div class="abs share-dot" style="left:249px"></div>
  <div class="abs share-dot" style="left:286px"></div>
  <div class="abs share-dot" style="left:323px"></div>
  <div class="abs cta">Call For Appointment</div>
</div>

<section class="abs panel" style="left:40px;top:545px;width:418px;height:206px">
  <h2 class="abs panel-title" style="left:12px;top:12px"><span class="small">Welcome to</span><br><span class="big">Delia's Dog Grooming</span></h2>
  <p class="abs copy" style="left:12px;top:73px;width:390px">
    <span class="line">Architecto beatae naseaeraciat kuiase undeosler miasosac usa</span>
    <span class="line">ntuedearsteked icexplic abo nemo enim ipsam lertasevol uptate-</span>
    <span class="line">mia voluptas sit. Aspernatur aut odit aut fugitedera quia conse-</span>
    <span class="line">quuntur magni dolores eosqui ratione voluptatem. Fequi</span>
    <span class="line">nesciunt neque porro quisquam estqui dolorem ipsumquia dolor</span>
    <span class="line end">sitamet. <span class="more">Read More</span></span>
  </p>
</section>

<section class="abs panel" style="left:484px;top:545px;width:418px;height:206px">
  <h2 class="abs panel-title" style="left:12px;top:12px"><span class="small">View our</span><br><span class="big">Grooming Gallery</span></h2>
  <svg class="arrow" style="left:12px;top:112px" width="22" height="42" viewBox="0 0 22 42"><path d="M19 3 L4 21 L19 39" fill="none" stroke="#8a8a8f" stroke-width="4" stroke-linecap="round"/></svg>
  <div class="abs thumb" style="left:50px;top:84px" role="img" aria-label="Schnauzer before grooming"><span class="tag">Before</span></div>
  <div class="abs thumb" style="left:218px;top:84px" role="img" aria-label="Schnauzer after grooming"><span class="tag">After</span></div>
  <svg class="arrow" style="left:382px;top:112px" width="22" height="42" viewBox="0 0 22 42"><path d="M3 3 L18 21 L3 39" fill="none" stroke="#8a8a8f" stroke-width="4" stroke-linecap="round"/></svg>
</section>

<section class="abs panel" style="left:40px;top:772px;width:566px;height:205px">
  <h2 class="abs panel-title" style="left:12px;top:14px"><span class="small">About</span> <span class="big">My Self</span></h2>
  <div class="abs" style="left:12px;top:57px;width:134px;height:114px;background:linear-gradient(#7c8a6a,#4e6b3a)" role="img" aria-label="Schnauzer sitting on a lawn"></div>
  <p class="abs copy" style="left:162px;top:51px;width:390px;line-height:21.4px">
    <span class="line">Architecto beatae naseaeraciat kuiase undeosler miasosac usa</span>
    <span class="line">ntuedearsteked icexplic abo nemo enim ipsam lertasevol uptate-</span>
    <span class="line">mia voluptas sit. Aspernatur aut odit aut fugitedera quia conse-</span>
    <span class="line">quuntur magni dolores eosqui ratione voluptatem. Fequi</span>
    <span class="line">nesciunt neque porro quisquam estqui dolorem ipsumquia dolor</span>
    <span class="line end">sitamet. <span class="more">Read More</span></span>
  </p>
</section>

<section class="abs panel" style="left:632px;top:772px;width:268px;height:268px">
  <h2 class="abs panel-title" style="left:13px;top:14px"><span class="small">Client's</span> <span class="big">Testimonials</span></h2>
  <div class="abs" style="left:14px;top:59px;width:77px;height:77px;border:4px solid #fff;box-shadow:0 1px 4px rgba(0,0,0,.35);background:linear-gradient(#8a6c4e,#2f2c2c)" role="img" aria-label="Client's schnauzer portrait"></div>
  <p class="abs copy" style="left:100px;top:57px;width:156px;font-size:11.8px;line-height:18.5px">
    <span class="line end">Architecto beatae nas-</span>
    <span class="line end">eaeraciat kuiase undeosler</span>
    <span class="line end">miasosac usa &nbsp;ntuedea</span>
    <span class="line end">rsteked icexplic abo nemo</span>
  </p>
  <p class="abs copy" style="left:13px;top:144px;width:245px;font-size:11.8px;line-height:18.5px">
    <span class="line">ipsam lertasevol uptatemia voluptas sit.</span>
    <span class="line">Aspernatur aut odit aut fugitedera quia con-</span>
    <span class="line end">sequuntur magni....</span>
  </p>
  <div class="abs" style="left:244px;top:207px;font-size:12px;color:var(--purple-text)">By</div>
  <div class="abs" style="left:13px;top:225px;font-size:12px"><span class="more" style="margin:0">Read More</span></div>
  <div class="abs" style="left:138px;top:225px;font-size:12px"><i>3 days ago</i> <span style="color:var(--purple-text);margin-left:4px">Dana Holt</span></div>
</section>

<div class="abs offer">
  <div class="abs offer-text">Special Offers for Dog's in<br>Delia's Dog Grooming. <i>FLAT 50% Off</i><br>on first five Customers !</div>
  <div class="abs offer-link">Click Here</div>
</div>
<div class="abs offer-photo" role="img" aria-label="Smiling schnauzer in a round frame"></div>

<footer class="abs footer">
  <div class="abs legal">Copyright © 2012 by Delia's Dog Grooming<br>All Right Reserved</div>
  <div class="abs links">Home &nbsp;|&nbsp; About Me &nbsp;|&nbsp; Services &nbsp;|&nbsp; Grooming &nbsp;|&nbsp; Gallery &nbsp;|&nbsp;Contact Me</div>
</footer>

</body>
</html>
```